MOLVT Study flyer

I need help designing a flyer for a research study that will include brain imaging in adolescents. The info is in the attached document. The study is called the Marrowby Orchard Lantern Vesper Trail (MOLVT) study. Ideally this would be returned as a document that I can edit in the future as we will have several new recruitment phases (different age groups, etc. I also would love to have a logo designed as part of this project, but I recognize that might be a separate design request.

```html
<!DOCTYPE html>
<html lang="en">
<head>
<meta charset="utf-8">
<title>MOLVT Study Flyer</title>
<link rel="stylesheet" href="https://fonts.googleapis.com/css2?family=Barlow+Semi+Condensed:wght@600;700;800&family=Nunito+Sans:wght@400;600;700&family=Dancing+Script:wght@600&display=swap">
<style>
  :root{
    --navy:#13235a;
    --purple:#5a3e96;
    --purple-soft:#9c82c4;
    --lavender:#ebe4f2;
    --lavender-mid:#d9cde9;
    --teal:#2f8c91;
    --teal-bright:#48c0c4;
    --teal-soft:#e2efee;
    --cream:#f7f5f0;
    --ink:#1f2230;
    --gold:#e3b02c;
    --gold-soft:#fbecc9;
    --white:#ffffff;
  }
  *{box-sizing:border-box;margin:0;padding:0}
  html,body{width:849px;height:1200px;overflow:hidden;background:var(--white)}
  body{font-family:"Nunito Sans",Arial,sans-serif;color:var(--ink)}
  .flyer{position:absolute;left:51px;top:51px;width:747px;height:1097px;background:var(--cream);overflow:hidden}
  .abs{position:absolute}
  .head{font-family:"Barlow Semi Condensed","Arial Narrow",sans-serif}

  .logo-mark{left:30px;top:22px;width:150px;height:150px;border-radius:50%;background:var(--lavender-mid)}
  .study-name{left:194px;top:20px;font-size:94px;font-weight:800;color:var(--navy);line-height:1;letter-spacing:1px}
  .study-full{left:199px;top:118px;font-size:20px;font-weight:700;line-height:26px;letter-spacing:.4px}
  .study-full .p{color:var(--purple)} .study-full .t{color:var(--teal)}

  .hero-photo{left:0;top:0;width:747px;height:470px}

  .hook{left:0;top:209px;width:450px;height:129px;background:var(--navy);border-radius:0 70px 0 0}
  .hook p{position:absolute;left:39px;top:16px;font-size:27px;font-weight:700;color:var(--white);line-height:33px;letter-spacing:.2px}
  .hook .hl{color:var(--teal-bright)}

  .intro-icon{left:38px;top:357px;width:92px;height:92px;border-radius:50%;background:var(--purple-soft)}
  .intro{left:151px;top:359px;width:380px;font-size:17px;line-height:26px}
  .intro strong{color:var(--purple);font-weight:700}

  .section-title{left:0;top:505px;width:747px;text-align:center;font-size:18px;font-weight:700;color:var(--purple);letter-spacing:.8px}
  .rule{top:514px;height:1.5px;background:var(--purple)}

  .step{top:530px;width:216px;text-align:center}
  .step .icon{width:108px;height:108px;border-radius:50%;margin:0 auto;display:flex;align-items:center;justify-content:center}
  .step h3{margin-top:6px;font-size:14.5px;font-weight:700;letter-spacing:.6px}
  .step p{font-size:12.8px;line-height:17px;margin-top:2px}
  .divider{top:540px;width:1px;height:204px;background:#c9d9dc}

  .eligible{left:0;top:762px;width:392px;height:186px;background:var(--teal-soft);border-radius:0 14px 14px 0}
  .head-art{left:14px;top:22px;width:120px;height:150px;border-radius:60px 60px 20px 40px;background:#cfe6e5}
  .eligible h4{position:absolute;left:129px;top:12px;font-size:14.5px;font-weight:700;color:var(--teal);letter-spacing:.5px}
  .checks{position:absolute;left:160px;top:40px;list-style:none;width:225px}
  .checks li{position:relative;padding-left:38px;font-size:13.6px;line-height:18px;margin-bottom:11px}
  .checks li svg{position:absolute;left:0;top:-2px}

  .contact{left:406px;top:762px;width:312px;height:186px;background:var(--lavender);border-radius:14px}
  .contact h4{position:absolute;left:30px;top:19px;font-size:17.5px;font-weight:700;color:var(--purple);line-height:21px;letter-spacing:.5px}
  .script{font-family:"Dancing Script",cursive;color:var(--teal);font-weight:600}
  .contact .script{position:absolute;left:30px;top:62px;font-size:33px}
  .contact .underline{position:absolute;left:106px;top:112px;width:150px;height:2px;background:var(--teal);border-radius:2px}
  .mail{position:absolute;left:22px;top:126px;width:48px;height:48px;border-radius:50%;background:var(--purple);display:flex;align-items:center;justify-content:center}
  .email{position:absolute;left:85px;top:139px;font-size:15.5px;font-weight:700;color:var(--navy)}

  .pay{left:82px;top:958px;width:582px;height:66px;background:var(--gold-soft);border-radius:18px}
  .pay .gift{position:absolute;left:42px;top:5px;width:56px;height:56px;border-radius:50%;border:2px solid var(--gold);display:flex;align-items:center;justify-content:center}
  .pay .label{position:absolute;left:118px;top:14px;font-size:31px;font-weight:800;color:var(--navy);letter-spacing:1.5px}
  .pay .script{position:absolute;left:345px;top:18px;font-size:24px;color:var(--purple)}
  .pay .amount{position:absolute;left:405px;top:10px;font-size:40px;font-weight:800;color:var(--purple);line-height:1}

  .footer{left:0;top:1030px;width:747px;height:67px;background:var(--navy)}
  .footer .seal{position:absolute;left:28px;top:14px;width:38px;height:40px;background:var(--gold);border-radius:4px}
  .footer p{position:absolute;left:80px;top:15px;color:var(--white);font-size:13px;line-height:18px}
</style>
</head>
<body>
<main class="flyer">
  <div class="abs hero-photo" role="img" aria-label="Photo of a thoughtful teenage girl in a lavender hoodie, chin resting on hand, beside a thought bubble with a tangled scribble and question mark">
    <svg width="747" height="470" viewBox="0 0 747 470">
      <defs>
        <linearGradient id="heroTone" x1="0" y1="0" x2="1" y2="1">
          <stop offset="0" stop-color="#e9e6ea"/>
          <stop offset=".5" stop-color="#c6b6d8"/>
          <stop offset="1" stop-color="#a996c4"/>
        </linearGradient>
      </defs>
      <path d="M435 0 H747 V464 C690 470 650 450 615 410 C590 380 570 360 520 338 L435 338 Z" fill="url(#heroTone)"/>
    </svg>
  </div>

  <div class="abs logo-mark"></div>
  <div class="abs study-name head">MOLVT</div>
  <div class="abs study-full head">
    <div class="p">MARROWBY ORCHARD</div>
    <div class="t">LANTERN VESPER TRAIL</div>
    <div class="p">STUDY</div>
  </div>

  <div class="abs hook head">
    <p>Are you the parent of a child<br>age 10–17? Do they <span class="hl">worry</span><br>or <span class="hl">overthink</span> negative emotions?</p>
  </div>

  <div class="abs intro-icon" role="img" aria-label="Brain icon"></div>
  <p class="abs intro">Harrowgate University researchers are seeking <strong>girls age 10–17</strong> for a study about brain activity in emotions and decision-making and how they relate to puberty, anxiety and depression.</p>

  <div class="abs rule" style="left:27px;width:193px"></div>
  <h2 class="abs section-title head">STUDY PARTICIPATION INVOLVES:</h2>
  <div class="abs rule" style="left:527px;width:193px"></div>

  <section class="abs step" style="left:20px">
    <div class="icon" style="background:var(--lavender-mid)">
      <svg width="70" height="62" viewBox="0 0 70 62" fill="none" stroke="#5a3e96" stroke-width="3">
        <rect x="3" y="12" width="52" height="36" rx="3"/><path d="M20 58h18M29 48v10"/>
        <circle cx="29" cy="26" r="5"/><path d="M19 42c2-6 18-6 20 0"/>
        <circle cx="56" cy="14" r="11" fill="#fff"/><path d="M51 14h10"/>
      </svg>
    </div>
    <h3 class="head" style="color:var(--purple)">ONE ONE-HOUR INTERVIEW</h3>
    <p>(online or in-person)<br>where your child will<br>discuss their thoughts.</p>
  </section>
  <div class="abs divider" style="left:250px"></div>
  <section class="abs step" style="left:246px">
    <div class="icon" style="background:#bfe2e0">
      <svg width="64" height="70" viewBox="0 0 64 70" fill="none" stroke="#2f8c91" stroke-width="3">
        <rect x="6" y="8" width="40" height="56" rx="3"/><rect x="18" y="3" width="16" height="9" rx="2" fill="#bfe2e0"/>
        <path d="M12 24l3 3 5-6M24 25h14M12 38l3 3 5-6M24 39h14M12 52l3 3 5-6M24 53h10"/>
        <path d="M58 18l-16 28-4 6 1-7 16-28z"/>
      </svg>
    </div>
    <h3 class="head" style="color:var(--teal)">ONLINE QUESTIONNAIRES</h3>
    <p>(parent and child).</p>
  </section>
  <div class="abs divider" style="left:460px"></div>
  <section class="abs step" style="left:471px">
    <div class="icon" style="background:var(--lavender-mid)">
      <svg width="76" height="64" viewBox="0 0 76 64" fill="none" stroke="#5a3e96" stroke-width="3">
        <path d="M22 60V30a28 28 0 0 1 56 0v30z" transform="translate(-6 0)"/>
        <circle cx="44" cy="32" r="12" fill="#5a3e96"/>
        <rect x="4" y="42" width="40" height="16" rx="3" fill="#d9cde9"/>
      </svg>
    </div>
    <h3 class="head" style="color:var(--purple)">ONE TWO-HOUR VISIT</h3>
    <p>where your child will complete<br>an MRI scan, answer questions<br>about their puberty stage,<br>and have a small hair sample<br>taken to study puberty hormones.</p>
  </section>

  <section class="abs eligible">
    <div class="abs head-art" role="img" aria-label="Line illustration of a head in profile with a brain"></div>
    <h4 class="head">YOUR CHILD MAY BE ELIGIBLE IF THEY:</h4>
    <ul class="checks">
      <li><svg width="26" height="26" viewBox="0 0 26 26"><circle cx="13" cy="13" r="13" fill="#2f8c91"/><path d="M7 13l4 4 8-8" stroke="#fff" stroke-width="2.6" fill="none"/></svg>Are age 10–17</li>
      <li><svg width="26" height="26" viewBox="0 0 26 26"><circle cx="13" cy="13" r="13" fill="#2f8c91"/><path d="M7 13l4 4 8-8" stroke="#fff" stroke-width="2.6" fill="none"/></svg>Tend to worry or<br>overthink negative thoughts</li>
      <li><svg width="26" height="26" viewBox="0 0 26 26"><circle cx="13" cy="13" r="13" fill="#2f8c91"/><path d="M7 13l4 4 8-8" stroke="#fff" stroke-width="2.6" fill="none"/></svg>Have not been diagnosed with psychosis, learning problems, or autism</li>
    </ul>
  </section>

  <section class="abs contact">
    <h4 class="head">INTERESTED IN PARTICIPATING?<br>WANT MORE INFORMATION?</h4>
    <div class="script">Please contact us!</div>
    <div class="underline"></div>
    <div class="mail"><svg width="28" height="20" viewBox="0 0 28 20" fill="none" stroke="#fff" stroke-width="2"><rect x="1" y="1" width="26" height="18" rx="2"/><path d="M1 2l13 10 13-10M1 19l10-9M27 19l-10-9"/></svg></div>
    <div class="email">molvtstudy@harrowgate-med.edu</div>
  </section>

  <section class="abs pay">
    <div class="gift"><svg width="28" height="28" viewBox="0 0 28 28" fill="#e3b02c"><rect x="2" y="9" width="24" height="6"/><rect x="4" y="15" width="20" height="12"/><rect x="12" y="9" width="4" height="18" fill="#fbecc9"/></svg></div>
    <div class="label head">COMPENSATION</div>
    <div class="script">up to</div>
    <div class="amount head">$140</div>
  </section>

  <footer class="abs footer">
    <div class="seal"></div>
    <p>A research study conducted by<br>Harrowgate University researchers</p>
  </footer>
</main>
</body>
</html>
```